Redesign Talent Management graphic

Need a new, fresh design approach to this graphic. Need it to be sized to fit into a widescreen PPT: 13.33in wide x 7.5in high. Looking for something clean and modern that will still get the message across that we offer products for every stage of the employment lifecycle.

Our brand color palette is red, gray, white, black. The red is PMS 186, or RGB 224, 0, 26.

Font styles to use
Sans Serif

```html
<!DOCTYPE html>
<html lang="en">
<head>
<meta charset="utf-8">
<title>Talent Management Tools for the Life Cycle of the Employee</title>
<link rel="stylesheet" href="https://fonts.googleapis.com/css2?family=Archivo:wght@800&family=Poppins:wght@700&display=swap">
<style>
  :root {
    --stage: #000000;
    --brand-red: #e31b3a;
    --grid-red: #ef4a5e;
    --band-light: #e8e8e9;
    --field-gray: #cbcbcd;
    --grid-gray: #dedee0;
    --ink-dark: #4a4a4c;
    --ink-black: #111111;
    --white: #ffffff;
    --figure-tone: rgba(20, 20, 20, 0.22);
  }
  html, body {
    margin: 0;
    padding: 0;
    width: 1200px;
    height: 993px;
    overflow: hidden;
    background: var(--stage);
  }
  .canvas { display: block; width: 1200px; height: 993px; }
  .title-main { font-family: "Poppins", sans-serif; font-weight: 700; fill: var(--white); }
  .title-sub { font-family: "Poppins", sans-serif; font-weight: 700; fill: var(--brand-red); }
  .title-tail { font-family: "Poppins", sans-serif; font-weight: 700; fill: var(--ink-dark); }
  .stage-label { font-family: "Archivo", sans-serif; font-weight: 800; font-size: 20px; fill: var(--ink-black); }
  .grid-line { stroke: var(--grid-gray); stroke-width: 6; }
  .grid-line-red { stroke: var(--grid-red); stroke-width: 5; }
  .growth-line { fill: var(--brand-red); }
  .milestone { fill: var(--white); }
  .stage-figure { fill: var(--figure-tone); }
</style>
</head>
<body>
<svg class="canvas" viewBox="0 0 1209 1000" preserveAspectRatio="none" xmlns="http://www.w3.org/2000/svg">
  <defs>
    <clipPath id="growth-clip">
      <polygon points="5,780 115,735 195,752 335,680 425,720 535,665 605,695 730,610 810,645 925,560 1005,605 1115,495 1209,585 1209,845 5,845"/>
    </clipPath>
  </defs>

  <!-- header band -->
  <rect x="5" y="170" width="1204" height="117" fill="var(--brand-red)"/>
  <rect x="5" y="287" width="1204" height="55" fill="var(--band-light)"/>
  <rect x="5" y="342" width="1204" height="503" fill="var(--field-gray)"/>

  <!-- background grid -->
  <g class="grid">
    <line class="grid-line" x1="90" y1="342" x2="90" y2="845"/>
    <line class="grid-line" x1="178" y1="342" x2="178" y2="845"/>
    <line class="grid-line" x1="262" y1="342" x2="262" y2="845"/>
    <line class="grid-line" x1="345" y1="342" x2="345" y2="845"/>
    <line class="grid-line" x1="430" y1="342" x2="430" y2="845"/>
    <line class="grid-line" x1="515" y1="342" x2="515" y2="845"/>
    <line class="grid-line" x1="603" y1="342" x2="603" y2="845"/>
    <line class="grid-line" x1="690" y1="342" x2="690" y2="845"/>
    <line class="grid-line" x1="775" y1="342" x2="775" y2="845"/>
    <line class="grid-line" x1="860" y1="342" x2="860" y2="845"/>
    <line class="grid-line" x1="945" y1="342" x2="945" y2="845"/>
    <line class="grid-line" x1="1030" y1="342" x2="1030" y2="845"/>
    <line class="grid-line" x1="1115" y1="342" x2="1115" y2="845"/>
    <line class="grid-line" x1="5" y1="430" x2="1209" y2="430"/>
    <line class="grid-line" x1="5" y1="520" x2="1209" y2="520"/>
    <line class="grid-line" x1="5" y1="610" x2="1209" y2="610"/>
    <line class="grid-line" x1="5" y1="700" x2="1209" y2="700"/>
    <line class="grid-line" x1="5" y1="790" x2="1209" y2="790"/>
  </g>

  <!-- rising growth chart -->
  <polygon class="growth-line" points="5,780 115,735 195,752 335,680 425,720 535,665 605,695 730,610 810,645 925,560 1005,605 1115,495 1209,585 1209,845 5,845"/>
  <g clip-path="url(#growth-clip)" opacity="0.6">
    <line class="grid-line-red" x1="90" y1="480" x2="90" y2="845"/>
    <line class="grid-line-red" x1="178" y1="480" x2="178" y2="845"/>
    <line class="grid-line-red" x1="345" y1="480" x2="345" y2="845"/>
    <line class="grid-line-red" x1="515" y1="480" x2="515" y2="845"/>
    <line class="grid-line-red" x1="690" y1="480" x2="690" y2="845"/>
    <line class="grid-line-red" x1="860" y1="480" x2="860" y2="845"/>
    <line class="grid-line-red" x1="1030" y1="480" x2="1030" y2="845"/>
    <line class="grid-line-red" x1="5" y1="520" x2="1209" y2="520"/>
    <line class="grid-line-red" x1="5" y1="610" x2="1209" y2="610"/>
    <line class="grid-line-red" x1="5" y1="700" x2="1209" y2="700"/>
    <line class="grid-line-red" x1="5" y1="790" x2="1209" y2="790"/>
  </g>

  <!-- milestones -->
  <g class="milestones">
    <rect class="milestone" x="108" y="741" width="14" height="14" transform="rotate(45 115 748)"/>
    <rect class="milestone" x="328" y="693" width="14" height="14" transform="rotate(45 335 700)"/>
    <rect class="milestone" x="528" y="673" width="14" height="14" transform="rotate(45 535 680)"/>
    <rect class="milestone" x="723" y="618" width="14" height="14" transform="rotate(45 730 625)"/>
    <rect class="milestone" x="920" y="571" width="14" height="14" transform="rotate(45 927 578)"/>
    <rect class="milestone" x="1108" y="510" width="14" height="14" transform="rotate(45 1115 517)"/>
  </g>

  <!-- heading -->
  <text class="title-main" x="32" y="272" font-size="76" textLength="983" lengthAdjust="spacingAndGlyphs">TALENT MANAGEMENT TOOLS</text>
  <text class="title-sub" x="35" y="331" font-size="46" textLength="787" lengthAdjust="spacing">FOR THE LIFE CYCLE</text>
  <text class="title-tail" x="33" y="410" font-size="80" textLength="630" lengthAdjust="spacingAndGlyphs">OF THE EMPLOYEE</text>

  <!-- stage illustrations -->
  <rect class="stage-figure" x="62" y="455" width="115" height="220" rx="8" role="img" aria-label="Illustration: businessman carrying a globe, representing recruitment and hiring"/>
  <rect class="stage-figure" x="255" y="480" width="120" height="165" rx="8" role="img" aria-label="Illustration: new employee relaxing in a red office chair, representing onboarding"/>
  <rect class="stage-figure" x="445" y="435" width="172" height="155" rx="8" role="img" aria-label="Illustration: speaker at a red podium addressing an audience, representing development"/>
  <rect class="stage-figure" x="655" y="375" width="145" height="170" rx="8" role="img" aria-label="Illustration: presenter pointing to a rising chart, representing high potential programs"/>
  <rect class="stage-figure" x="855" y="335" width="135" height="165" rx="8" role="img" aria-label="Illustration: man carrying a large red flag, representing succession planning"/>
  <rect class="stage-figure" x="1030" y="285" width="170" height="155" rx="8" role="img" aria-label="Illustration: two businessmen shaking hands, representing business"/>

  <!-- stage labels -->
  <g class="stage-labels">
    <text class="stage-label" x="47" y="703">RECRUITMENT</text>
    <text class="stage-label" x="47" y="723">AND HIRING</text>
    <text class="stage-label" x="252" y="667">ON BOARDING</text>
    <text class="stage-label" x="466" y="614">EMPLOYEE &amp;</text>
    <text class="stage-label" x="466" y="634">LEADERSHIP</text>
    <text class="stage-label" x="466" y="654">DEVELOPMENT</text>
    <text class="stage-label" x="653" y="572">HIGH POTENTIAL</text>
    <text class="stage-label" x="653" y="592">PROGRAMS</text>
    <text class="stage-label" x="870" y="529">SUCCESSION</text>
    <text class="stage-label" x="870" y="549">PLANNING</text>
    <text class="stage-label" x="1072" y="481">BUSINESS</text>
  </g>
</svg>
</body>
</html>
```